Labels for an activated Charcoal Facial Wash, Scrub and Mask

We need a new label design for a new line of Facial products. The product, falls under our Brand Lumivo and is based on Activated Charcoal. Activated Black Charcoal Facial wash (250ml), Activated Black Charcoal Mask (100gms) and Activated Black Charcoal face scrub (100gms). We would like to see designs that are modern, clean and must communicate natural products.

```html
<!DOCTYPE html>
<html lang="en">
<head>
<meta charset="utf-8">
<title>Lumivo Activated Black Charcoal Facial Wash Label</title>
<link href="https://fonts.googleapis.com/css2?family=Oswald:wght@400;500&family=Allura&display=swap" rel="stylesheet">
<style>
  :root {
    --backdrop: #d9d9d9;
    --label-white: #ffffff;
    --charcoal: #231f20;
    --olive-type: #5a604b;
    --cream-script: #dcdaa8;
    --olive-band: #4a4f3e;
    --band-type: #d4d2a4;
    --cap-khaki: #c3c398;
    --brand-olive: #3a3d30;
    --frame-line: #b9b78a;
  }
  * { margin: 0; padding: 0; box-sizing: border-box; }
  html, body { width: 1200px; height: 900px; overflow: hidden; }
  body {
    background: var(--backdrop);
    display: flex;
    align-items: center;
    justify-content: center;
  }
  .label {
    position: relative;
    width: 390px;
    height: 840px;
    background: var(--charcoal);
    overflow: hidden;
  }
  .label__top {
    position: absolute;
    inset: 0 0 auto 0;
    height: 200px;
    background: var(--label-white);
  }
  .brand {
    position: absolute;
    top: 60px;
    left: 50%;
    transform: translateX(-50%);
    width: 162px;
    height: 130px;
    display: flex;
    align-items: flex-end;
    justify-content: center;
    gap: 10px;
    padding-bottom: 18px;
  }
  .brand__square {
    width: 10px;
    height: 10px;
    background: var(--frame-line);
    margin-bottom: 8px;
  }
  .brand__name {
    font-family: "Oswald", sans-serif;
    font-weight: 400;
    font-size: 22px;
    letter-spacing: 6px;
    color: var(--brand-olive);
    text-transform: uppercase;
  }
  .label__texture {
    position: absolute;
    top: 195px;
    left: 0;
    width: 100%;
    height: 150px;
    background: linear-gradient(to bottom, var(--label-white) 0%, #9a9899 40%, var(--charcoal) 100%);
  }
  .product-name {
    position: absolute;
    top: 385px;
    left: 0;
    width: 100%;
    text-align: center;
    line-height: 1;
  }
  .product-name__script {
    font-family: "Allura", cursive;
    font-size: 58px;
    color: var(--cream-script);
    display: block;
  }
  .product-name__script--top { margin-bottom: -14px; }
  .product-name__script--bottom { margin-top: -12px; }
  .product-name__black {
    font-family: "Oswald", sans-serif;
    font-weight: 500;
    font-size: 118px;
    color: var(--olive-type);
    display: block;
    transform: scaleX(0.78);
    letter-spacing: 1px;
    line-height: 0.95;
  }
  .product-name__charcoal {
    font-family: "Oswald", sans-serif;
    font-weight: 500;
    font-size: 64px;
    color: var(--olive-type);
    display: block;
    transform: scaleX(0.74);
    line-height: 0.95;
  }
  .volume-band {
    position: absolute;
    top: 657px;
    left: 0;
    width: 100%;
    height: 34px;
    background: var(--olive-band);
    display: flex;
    align-items: center;
    justify-content: center;
    font-family: "Oswald", sans-serif;
    font-weight: 500;
    font-size: 17px;
    letter-spacing: 1px;
    color: var(--band-type);
  }
  .label__cap {
    position: absolute;
    top: 698px;
    left: 0;
    width: 100%;
    height: 142px;
    background: var(--cap-khaki);
  }
</style>
</head>
<body>
  <main class="label">
    <div class="label__top">
      <div class="brand">
        <span class="brand__square"></span>
        <span class="brand__name">Lumivo</span>
      </div>
    </div>
    <div class="label__texture" role="img" aria-label="Scattered charcoal powder texture fading from white into black"></div>
    <h1 class="product-name">
      <span class="product-name__script product-name__script--top">Activated</span>
      <span class="product-name__black">BLACK</span>
      <span class="product-name__charcoal">CHARCOAL</span>
      <span class="product-name__script product-name__script--bottom">Facial wash</span>
    </h1>
    <div class="volume-band">250ML</div>
    <div class="label__cap"></div>
  </main>
</body>
</html>
```